perforated vinyl window art

I am Franchise owner that needs to keep with the corporate image and logo requirements. The business is insurance and we are a store front office. I want to incorporate the following:
•The Allmutuals (like brook acre) and my individual office name Ridgevale Tonbury Insurance ltd.
•Chinese Version on Left door
•Modern looking
•Top of doors and same space on top of two windows needs to have Insurance Financial Services. I want the text to be a similar font to provided images.
•Mid part of the windows should be free of anything, so I can have more sunlight in my office. If part of a picture or letter was in the centre but originated in the bottom, that is fine, and maybe preferred.

Target Market(s)

our webpage is www.allmutualsgrp.ca under the about us, has logo's and usage there. The look and feel of the window art should look similar to this. Also, see attached pictures. The Ridgevale Tonbury insurance in Gold is my prefered logo for my company under The Allmutuals. The window picture is only for sizing and to give you a very rough idea. I have also included another design from a different office, I like the feel of this, but wantt to make it more specific to my office.

Industry/Entity Type

Insurance

Requirements
Must have
• •The Allmutuals (like brook acre) and my individual office name Ridgevale Tonbury Insurance ltd.
•Modern looking
- Should also include royalty free images, or paid for images.
- Include hours of operation - Monday to Friday 9am - 5pm
- Include address #238 14620-72 ave
- Phone number 780-555-0193

```html
<!DOCTYPE html>
<html lang="en">
<head>
<meta charset="utf-8">
<title>Ridgevale Tonbury Insurance Ltd. – Window Art</title>
<link rel="stylesheet" href="https://fonts.googleapis.com/css2?family=Open+Sans:wght@400;600;700&display=swap">
<style>
  :root {
    --gold: #d9ab5f;
    --glass: #2f3136;
    --frame: #4a3b32;
    --backdrop: #e9e7e3;
  }
  * { box-sizing: border-box; margin: 0; padding: 0; }
  html, body { width: 1200px; height: 893px; overflow: hidden; }
  body {
    position: relative;
    background: var(--backdrop);
    font-family: "Open Sans", Arial, sans-serif;
    color: var(--gold);
  }
  .pane {
    position: absolute;
    background: var(--glass);
    border: 4px solid var(--frame);
    overflow: hidden;
  }
  .headline {
    position: absolute;
    left: 0; right: 0;
    text-align: center;
    font-weight: 600;
    font-size: 45px;
    line-height: 1;
  }
  .service-list {
    position: absolute;
    left: 0; right: 0;
    text-align: center;
    font-size: 18px;
    letter-spacing: 0.5px;
  }

  /* Transom above the doors */
  .transom { left: 52px; top: 166px; width: 494px; height: 78px; }
  .transom .headline { top: 14px; left: 140px; right: 0; }
  .transom-mark {
    position: absolute; left: 18px; top: 12px;
    width: 46px; height: 46px; border-radius: 50%;
    background: var(--gold);
  }

  /* Windows */
  .window-left  { left: 563px; top: 166px; width: 274px; height: 522px; }
  .window-right { left: 851px; top: 166px; width: 292px; height: 522px; }
  .window .headline { top: 16px; }
  .window .service-list { top: 66px; }
  .roof, .pointer { position: absolute; }
  .roof { top: 136px; }
  .pointer { top: 298px; }

  .tagline {
    position: absolute; top: 210px;
    width: 190px; height: 90px;
  }
  .tagline .big {
    position: absolute; left: 0;
    font-size: 33px; font-weight: 700; line-height: 1;
    white-space: nowrap;
  }
  .tagline .coverage  { top: 0; }
  .tagline .important { top: 36px; }
  .tagline .for-the {
    position: absolute; left: 190px; top: 4px;
    font-size: 15px; font-weight: 600; line-height: 18px;
    letter-spacing: 1px;
    transform: rotate(90deg); transform-origin: left top;
    white-space: nowrap;
  }
  .tagline .life {
    position: absolute; right: 0; top: 76px;
    font-size: 18px; font-weight: 600; line-height: 1;
    white-space: nowrap;
  }

  .photo-frame {
    position: absolute; border: 3px solid var(--gold); border-radius: 12px;
  }

  /* Doors */
  .door { top: 292px; width: 192px; height: 480px; }
  .door-left  { left: 86px; }
  .door-right { left: 328px; }
  .door-text { position: absolute; left: 0; right: 0; text-align: center; }
  .chinese-label { top: 20px; font-size: 19px; font-weight: 600; }
  .phone { top: 92px; font-size: 19px; font-weight: 600; }
  .hours { top: 133px; font-size: 16px; font-weight: 600; line-height: 1.1; }
  .office-name {
    position: absolute; left: 46px; top: 16px; width: 140px;
    font-size: 12px; font-weight: 400; line-height: 1.3;
    text-transform: uppercase; letter-spacing: 0.3px;
  }
  .office-mark {
    position: absolute; left: 8px; top: 18px;
    width: 32px; height: 32px; border-radius: 50%; background: var(--gold);
  }
  .door-photo { position: absolute; left: 0; right: 0; top: 176px; bottom: 0; }
</style>
</head>
<body>

  <section class="pane transom">
    <span class="transom-mark"></span>
    <h1 class="headline">Insurance</h1>
  </section>

  <section class="pane door door-left">
    <p class="door-text chinese-label">Chinese Version</p>
    <p class="door-text phone">780.555.0193</p>
    <p class="door-text hours">Monday to Friday<br>9:00 am to 5:00 pm</p>
    <div class="door-photo" role="img" aria-label="Portrait of a smiling insurance advisor in a dark business suit"
         style="background: linear-gradient(180deg, #5c7c95 0%, #3c4e5e 40%, #1f2124 100%);"></div>
  </section>

  <section class="pane door door-right">
    <span class="office-mark"></span>
    <p class="office-name">Ridgevale Tonbury<br>Insurance Ltd.</p>
    <p class="door-text phone">780.555.0193</p>
    <p class="door-text hours">Monday to Friday<br>9:00 am to 5:00 pm</p>
    <div class="door-photo" role="img" aria-label="Family of four lying on the grass, framed by a gold house outline"
         style="background: linear-gradient(160deg, #6f9a4a 0%, #b9b3a8 45%, #5d8a3c 100%);"></div>
  </section>

  <section class="pane window window-left">
    <h2 class="headline">Financial</h2>
    <p class="service-list">Auto | Home | Business</p>
    <svg class="roof" style="left:41px" width="184" height="68" viewBox="0 0 184 68"><polygon points="92,0 184,68 0,68" fill="var(--gold)"/></svg>
    <div class="tagline" style="left:40px">
      <span class="big coverage">Coverage</span>
      <span class="big important">important</span>
      <span class="for-the">for the</span>
      <span class="life">things in life</span>
    </div>
    <svg class="pointer" style="left:40px" width="56" height="34" viewBox="0 0 56 34"><polygon points="0,0 56,0 28,34" fill="var(--gold)"/></svg>
    <div class="photo-frame" role="img" aria-label="Happy family outdoors, children riding on parents' shoulders"
         style="left:5px; top:332px; width:262px; height:170px; background: linear-gradient(160deg, #a9c98a 0%, #6f9a4a 55%, #d8c8b4 100%);"></div>
  </section>

  <section class="pane window window-right">
    <h2 class="headline">Services</h2>
    <p class="service-list">Life | Investments | Travel</p>
    <svg class="roof" style="left:50px" width="184" height="68" viewBox="0 0 184 68"><polygon points="92,0 184,68 0,68" fill="var(--gold)"/></svg>
    <div class="tagline" style="left:46px">
      <span class="big coverage">Coverage</span>
      <span class="big important">important</span>
      <span class="for-the">for the</span>
      <span class="life">things in life</span>
    </div>
    <svg class="pointer" style="left:46px" width="56" height="34" viewBox="0 0 56 34"><polygon points="0,0 56,0 28,34" fill="var(--gold)"/></svg>
    <div class="photo-frame" role="img" aria-label="Cupped hands sheltering a small model house with a red roof"
         style="left:12px; top:332px; width:264px; height:170px; background: linear-gradient(160deg, #e9c9a8 0%, #d9a582 50%, #c98c6a 100%);"></div>
  </section>

</body>
</html>
```